Quellmar Aus Business card revamp

We are looking to revamp our business card design. We are hoping to change our colours to dark navey blue, gray, white and black but are open to keeping the same if a good design is submited. We are after somthing a bit differnt not just boring business card. I have attached a copy of our current card. We Want to keep the same logo design which i have attached a few to hopfully help you in this process. We are after a design that can be personalized to separate 4 people

Industry/Entity Type

Business

Colors
0455a3
ffffff
000000
cbcbcb

Requirements
Must have
• Quellmar Logo, address 3/41 Wattlebend Street, Kelvanby 4517, phone number, Name and position

```html
<!DOCTYPE html>
<html lang="en">
<head>
<meta charset="utf-8">
<title>Quellmar Aus – Business Card</title>
<link href="https://fonts.googleapis.com/css2?family=Open+Sans:wght@400;600;700;800&display=swap" rel="stylesheet">
<style>
  :root {
    --backdrop: #e4e4e4;
    --card-dark: #2b2c2e;
    --card-light: #f6f6f6;
    --brand-blue: #2f7fc1;
    --brand-orange: #f07a22;
    --ink: #2a2a2a;
    --ink-soft: #3a3a3a;
    --on-dark: #e8e8e8;
  }
  * { box-sizing: border-box; margin: 0; padding: 0; }
  html, body { width: 1200px; height: 576px; overflow: hidden; }
  body {
    background: var(--backdrop);
    font-family: "Open Sans", sans-serif;
    position: relative;
  }
  .card {
    position: absolute;
    top: 138px;
    width: 484px;
    height: 293px;
    border-radius: 14px;
    box-shadow: 0 3px 6px rgba(0,0,0,.25);
    overflow: hidden;
  }
  .card--front { left: 82px; background: var(--card-dark); }
  .card--back { left: 602px; background: var(--card-light); }

  .brand { position: absolute; display: flex; flex-direction: column; }
  .brand__name {
    display: flex; align-items: center; gap: 8px;
    font-weight: 800; color: var(--brand-blue); line-height: 1;
  }
  .brand__dot { border-radius: 50%; background: var(--brand-orange); flex: none; }
  .brand__tagline { font-weight: 800; color: var(--brand-blue); line-height: 1.1; }

  .card--front .brand { left: 0; right: 0; top: 98px; align-items: center; }
  .card--front .brand__name { font-size: 46px; }
  .card--front .brand__dot { width: 30px; height: 30px; }
  .card--front .brand__tagline { font-size: 16px; margin-top: 4px; }

  .front__web {
    position: absolute; left: 0; right: 0; top: 266px;
    display: flex; justify-content: center; align-items: center; gap: 22px;
    color: var(--on-dark); font-size: 13px;
  }
  .front__rule { width: 48px; height: 2px; background: var(--brand-orange); }

  .card--back .brand { left: 26px; top: 34px; }
  .card--back .brand__name { font-size: 34px; }
  .card--back .brand__dot { width: 22px; height: 22px; }
  .card--back .brand__tagline { font-size: 12px; margin-top: 3px; padding-left: 30px; }

  .person { position: absolute; left: 26px; top: 129px; }
  .person__name { font-size: 19px; font-weight: 700; color: var(--ink); }
  .person__role { font-size: 10.5px; color: var(--ink-soft); margin-top: 2px; }

  .contact { position: absolute; left: 26px; top: 198px; list-style: none; }
  .contact li {
    display: flex; align-items: center; gap: 8px;
    font-size: 12.5px; color: var(--ink); height: 16px;
  }
  .contact li.contact__address { margin-top: 4px; }
  .contact svg { width: 10px; height: 10px; fill: var(--brand-orange); flex: none; }
  .contact .accent { color: var(--brand-blue); }

  .services { position: absolute; left: 278px; top: 178px; list-style: none; }
  .services li {
    display: flex; align-items: center; gap: 8px;
    font-size: 12.5px; font-weight: 600; color: var(--ink); height: 16px;
  }
  .services li::before {
    content: "»"; color: var(--brand-orange); font-weight: 700; font-size: 13px;
  }
</style>
</head>
<body>

<section class="card card--front">
  <div class="brand">
    <div class="brand__name"><span class="brand__dot"></span>Quellmar</div>
    <div class="brand__tagline">Passive Fire Protection</div>
  </div>
  <div class="front__web">
    <span class="front__rule"></span>
    <span>www.quellmar.com.au</span>
    <span class="front__rule"></span>
  </div>
</section>

<section class="card card--back">
  <div class="brand">
    <div class="brand__name"><span class="brand__dot"></span>Quellmar</div>
    <div class="brand__tagline">Passive Fire Protection</div>
  </div>

  <div class="person">
    <h1 class="person__name">Employee Name</h1>
    <p class="person__role">Managing Director</p>
  </div>

  <ul class="contact">
    <li>
      <svg viewBox="0 0 10 10"><path d="M1 3c0-1 1-2 4-2s4 1 4 2v1H7V3H3v1H1zM2 5h6l1 4H1z"/></svg>
      07 3418 2265
    </li>
    <li>
      <svg viewBox="0 0 10 10"><circle cx="5" cy="5" r="4.5"/><path d="M.5 5h9M5 .5v9" stroke="#f6f6f6" stroke-width=".8"/></svg>
      www.<span class="accent">quellmar</span>.com.au
    </li>
    <li>
      <svg viewBox="0 0 10 10"><rect x="0" y="2" width="10" height="6.5"/><path d="M0 2l5 4 5-4" fill="none" stroke="#f6f6f6" stroke-width=".8"/></svg>
      enquiries@quellmar.com.au
    </li>
    <li class="contact__address">3/41 Wattlebend Street, Kelvanby 4517</li>
  </ul>

  <ul class="services">
    <li>Service Penetrations</li>
    <li>Steel Spray Coatings</li>
    <li>Intumescent Paint</li>
    <li>Duct Spray &amp; Wraps</li>
    <li>Fire &amp; Smoke Bankers</li>
    <li>Pro Steel Walls &amp; Coationgs</li>
  </ul>
</section>

</body>
</html>
```